Luxury Real Estate Website, Midwest, United States

We need web design services for a luxury website. We need IDX Integration with our MLS. We want this to be a very simple website with amazing graphics. We want it to link up with our MailChimp account in order to generate leads through a "More Information" Pop up on the main page. We want the main page to be covered with one large graphic that is a rolling slideshow of active listings of $400,000 and up from the IDX Integration. We need this website to give a very exclusive and sleek look. Lots of black is good... I will upload our logos in Black and Silver. We will also need an "About" page that we are going to call "ZenPO Info". We want our graphics to be extremely impressive. Keep in mind, we are a company in the Midwest of the United States, and our real estate has a different look than homes in California or Florida. We need graphics that are realistic for the Midwest, yet still high-end.
Target Market(s)
Luxury Homeowners in the Midwest United States. The graphics needs to be pristine.
Industry/Entity Type
Real Estate
Coding
Coded - Design and coding required
Number of Pages Required
3 page
Requirements
Must have
- Large graphics with IDX Integration. The photos of real estate need to represent real estate that is common in the Midwest, United States. We also need MailChimp integration. We need a pop up that is titled "My Free Market Analysis" that makes them fill out a contact form asking for Full Name, Email Address, Phone Number and Address. This needs to be a pop up on the front page and will integrate with our MailChimp account. We also need a page called "About Zen PO Home". And another page where clients can download informational PDFs. The main component needs to be a front page search engine connected with the IDX to access active listings from our MLS. I attached our logos and a sample front page of a website. I would love for ours to look similar.
Nice to have
- Lake House photos on midwest lakes are a plus.
Should not have
- Should not have clutter. This website needs to be clean, luxurious and exclusive.

```html
<!DOCTYPE html>
<html lang="en">
<head>
<meta charset="utf-8">
<title>Northvale Realty Group</title>
<link href="https://fonts.googleapis.com/css2?family=Ubuntu:wght@400;500;700&display=swap" rel="stylesheet">
<style>
:root{
  --ink:#1b1b1b;
  --text:#555;
  --blue:#1a56c4;
  --blue-dark:#164aa8;
  --about-bg:#c1d1e6;
  --contact-bg:#ebebeb;
  --white:#fff;
  --rule:#444;
}
*{box-sizing:border-box;margin:0;padding:0}
html,body{width:810px;height:1200px;overflow:hidden}
body{font-family:'Ubuntu',sans-serif;color:var(--ink);background:var(--white);position:relative}
.abs{position:absolute}

.site-header{position:absolute;left:0;top:0;width:810px;height:50px;background:var(--white)}
.brand{position:absolute;left:64px;top:14px;display:flex;align-items:center;gap:6px;font-size:14px;font-weight:500;letter-spacing:.5px;color:var(--ink)}
.brand-mark{width:10px;height:10px;background:var(--ink)}
.main-nav{position:absolute;left:328px;top:21px;display:flex;gap:24px;font-size:7px;font-weight:500;text-transform:uppercase}
.account{position:absolute;left:693px;top:21px;font-size:7px;font-weight:500}
.account .sign{color:var(--blue)}

.hero{position:absolute;left:0;top:50px;width:810px;height:344px;
  background:linear-gradient(180deg,#6f8fc4 0%,#a9bcd6 28%,#6e8a3a 52%,#4f7a2a 68%,#59656a 82%,#3f4a45 100%)}
.search-tabs{position:absolute;left:142px;top:182px;display:flex;gap:4px}
.tab{height:22px;padding:0 15px;border-radius:4px 4px 0 0;font-size:10.5px;font-weight:500;line-height:22px}
.tab.active{background:#111;color:var(--white)}
.tab.alt{background:#c1d1e6;color:var(--ink);width:161px;text-align:center}
.search-band{position:absolute;left:142px;top:204px;width:538px;height:54px;background:rgba(0,0,0,.85)}
.search-input{position:absolute;left:8px;top:11px;width:492px;height:31px;background:var(--white);border-radius:3px 0 0 3px;font-size:8px;color:#666;padding:11px 10px}
.search-btn{position:absolute;left:500px;top:11px;width:29px;height:31px;background:#d9e2ef;border-radius:0 3px 3px 0}
.side-tab{position:absolute;top:204px;width:30px;height:91px;background:var(--blue);color:var(--white);font-size:10px;font-weight:500;display:flex;align-items:center;justify-content:center}
.side-tab span{writing-mode:vertical-rl;transform:rotate(180deg);letter-spacing:.5px}
.side-tab.right span{transform:none;writing-mode:vertical-rl;transform:rotate(180deg)}
.live-chat{left:0}
.feedback{left:780px}

.section-title{position:absolute;left:0;width:810px;text-align:center;font-size:14px;font-weight:500;text-transform:uppercase}
.section-rule{position:absolute;left:382px;width:46px;height:2px;background:var(--rule)}

.about{position:absolute;left:0;top:394px;width:810px;height:226px;background:var(--about-bg)}
.about p{position:absolute;left:148px;top:86px;width:514px;text-align:center;font-size:7.6px;line-height:15px;color:var(--text)}
.btn{position:absolute;background:var(--blue);color:var(--white);font-size:8px;font-weight:500;text-transform:uppercase;display:flex;align-items:center;justify-content:center}

.projects{position:absolute;left:0;top:620px;width:810px;height:253px;background:var(--white)}
.project{position:absolute;top:76px;width:209px;height:134px}
.project-1{left:74px;background:linear-gradient(160deg,#2d3a25,#5b3a2c 55%,#1f2a1c)}
.project-2{left:300px;background:linear-gradient(180deg,#5f8fc6,#9dbadb 40%,#6b3b24 65%,#4a6a2a)}
.project-3{left:526px;background:linear-gradient(180deg,#1f46a8,#3f5db8 45%,#b08a4a 65%,#4a4470)}
.project-caption{position:absolute;left:0;top:56px;width:209px;text-align:center;color:var(--white);font-size:10px;font-weight:500}
.project-btn{position:absolute;left:64px;top:76px;width:84px;height:15px;background:var(--blue);color:var(--white);font-size:7px;font-weight:500;display:flex;align-items:center;justify-content:center}

.contact{position:absolute;left:0;top:873px;width:810px;height:267px;background:var(--contact-bg)}
.field{position:absolute;background:var(--white);font-size:8px;color:#777;padding:0 8px;display:flex;align-items:center}
.field.message{align-items:flex-start;padding-top:12px}
.req{color:var(--blue)}
.info{position:absolute;left:518px;font-size:8px;color:var(--ink)}
.info.phone{font-size:19px;font-weight:400}
.icon{position:absolute}

.site-footer{position:absolute;left:0;top:1140px;width:810px;height:60px;background:var(--white)}
.footer-nav{position:absolute;left:422px;top:26px;display:flex;gap:24px;font-size:7px;font-weight:500;text-transform:uppercase}
</style>
</head>
<body>

<header class="site-header">
  <div class="brand"><span>NORTHVALE REALTY</span><span class="brand-mark"></span></div>
  <nav class="main-nav"><span>Home</span><span>ZenPO Info</span><span>About Zen PO Home</span><span>Downloads</span><span>Contact Us</span></nav>
  <div class="account"><span class="sign">SIGN IN</span> | LOGIN</div>
</header>

<section class="hero" role="img" aria-label="Brick lake house with steep tiled roof among trees, reflected in a calm pond at sunset">
</section>
<div class="search-tabs">
  <div class="tab active">Search Homes</div>
  <div class="tab alt">What's Your Home Worth</div>
</div>
<div class="search-band">
  <div class="search-input">Search homes by city &amp; State,zip or MLS #</div>
  <div class="search-btn">
    <svg width="29" height="31" viewBox="0 0 29 31"><circle cx="16" cy="14" r="5.5" fill="none" stroke="#222" stroke-width="1.3"/><line x1="12" y1="18" x2="8" y2="22" stroke="#222" stroke-width="1.5"/></svg>
  </div>
</div>
<div class="side-tab live-chat"><span>LIVE CHAT</span></div>
<div class="side-tab feedback right"><span>FEEDBACK</span></div>

<section class="about">
  <h2 class="section-title" style="top:46px">About Zen PO Home</h2>
  <div class="section-rule" style="top:72px"></div>
  <p>Sed ut perspiciatis unde omnis iste natus error sit voluptatem accusantium doloremque laudantium, totam rem aperiam, eaque ipsa quae ab illo inventore veritatis et quasi architecto beatae vitae dicta sunt explicabo. Nemo enim ipsam voluptatem quia voluptas sit aspernatur aut odit aut fugit, sed quia consequuntur magni dolores eos qui ratione voluptatem sequi nesciunt. Neque porro quisquam est, qui dolorem ipsum quia dolor sit amet</p>
  <div class="btn" style="left:347px;top:163px;width:116px;height:29px">Read More</div>
</section>

<section class="projects">
  <h2 class="section-title" style="top:33px">Projects</h2>
  <div class="section-rule" style="top:58px"></div>
  <div class="project project-1" role="img" aria-label="Red wooden cabin with porch in a dense forest">
    <div class="project-caption">Sed ut perspiciatis unde omni</div>
    <div class="project-btn">VIEW DETAILS</div>
  </div>
  <div class="project project-2" role="img" aria-label="Dark timber lake cottage on a green lawn by the water"></div>
  <div class="project project-3" role="img" aria-label="Large illuminated stone home with driveway at dusk"></div>
</section>

<section class="contact">
  <h2 class="section-title" style="top:26px">Contact Us</h2>
  <div class="section-rule" style="top:51px"></div>
  <div class="field" style="left:66px;top:78px;width:198px;height:33px">Name&nbsp;<span class="req">*</span></div>
  <div class="field" style="left:66px;top:121px;width:198px;height:33px">E-Mail&nbsp;<span class="req">*</span></div>
  <div class="field" style="left:66px;top:162px;width:198px;height:34px">Phone&nbsp;<span class="req">*</span></div>
  <div class="field message" style="left:276px;top:78px;width:198px;height:118px">Message</div>
  <div class="btn" style="left:382px;top:202px;width:92px;height:34px">Send</div>

  <svg class="icon" style="left:493px;top:84px" width="9" height="12" viewBox="0 0 9 12"><path d="M4.5 0C2 0 0 2 0 4.5 0 7.5 4.5 12 4.5 12S9 7.5 9 4.5C9 2 7 0 4.5 0Z" fill="var(--blue)"/><circle cx="4.5" cy="4.5" r="1.7" fill="var(--contact-bg)"/></svg>
  <div class="info" style="top:85px">Northvale Office</div>
  <div class="info" style="top:104px">218 Lakeview Avenue | Madison, WI 53703</div>

  <svg class="icon" style="left:492px;top:141px" width="11" height="8" viewBox="0 0 11 8"><rect width="11" height="8" fill="#111"/><path d="M0 0 5.5 4.5 11 0" fill="none" stroke="var(--contact-bg)" stroke-width="1"/></svg>
  <div class="info" style="top:140px">E-Mail: hello@northvale-realty.com</div>

  <svg class="icon" style="left:493px;top:178px" width="10" height="10" viewBox="0 0 10 10"><path d="M2 0 4 2.5 3 4C3.8 5.6 4.6 6.4 6 7L7.5 6 10 8 8.5 10C4 9.5 0.5 6 0 1.5Z" fill="#111"/></svg>
  <div class="info phone" style="top:168px">1-800-555-0148</div>
</section>

<footer class="site-footer">
  <div class="brand" style="left:69px;top:22px"><span>NORTHVALE REALTY</span><span class="brand-mark"></span></div>
  <nav class="footer-nav"><span>Home</span><span>ZenPO Info</span><span>About Zen PO Home</span><span>Downloads</span><span>Contact Us</span><span style="margin-left:10px">CS</span></nav>
</footer>

</body>
</html>
```